Home care support

Design a a great and dynamic website for a healthcare business. Our business will be involved in providing care at home for people with disability and the elderly. Below is a link that I found for a company offering similar services in the US. I am looking for something like this .
I have my files - the latest project in here in through through Pixelmarket
Sample site : https://cedarbrookassistedliving.com/
Target Market(s)
people with disability and elderly seniors who need home care support
Industry/Entity Type
Health
Coding
Coded - Design and coding required
Number of Pages Required
5+ page
Requirements
Must have
- inspirational pictures and designed with the themed logo (files attached)
Nice to have
- This is my sample and should look like this : https://cedarbrookassistedliving.com/

```html
<!DOCTYPE html>
<html lang="en">
<head>
<meta charset="utf-8">
<title>Maplerose Healthcare</title>
<link href="https://fonts.googleapis.com/css2?family=Libre+Baskerville:wght@700&family=Poppins:wght@400;500;600&display=swap" rel="stylesheet">
<style>
:root{
  --blue:#0b69a3;
  --blue-dark:#0a4f7c;
  --green:#5f9a3d;
  --green-soft:#eef5e7;
  --ink:#161616;
  --body:#444;
  --sky:#eef7fc;
  --line:#e6e9ec;
}
*{box-sizing:border-box;margin:0;padding:0}
html,body{width:1200px;height:3704px;overflow:hidden}
body{position:relative;font-family:"Poppins",sans-serif;color:var(--body);background:#fff}
.abs{position:absolute}
.serif{font-family:"Libre Baskerville",serif;font-weight:700;color:var(--ink)}
.btn{position:absolute;display:flex;align-items:center;justify-content:center;background:var(--green);color:#fff;font-weight:600;font-size:14px;border-radius:3px;letter-spacing:.2px}

/* header */
.site-header{position:absolute;left:0;top:0;width:1200px;height:125px;background:var(--blue);z-index:5}
.brand{position:absolute;display:flex;align-items:center;gap:14px;color:#fff;font-family:"Libre Baskerville",serif;font-weight:700}
.brand .dot{border-radius:50%;border:6px solid #fff;flex:none}
.call{left:680px;top:16px;display:flex;gap:14px;align-items:center;color:#fff}
.call small{display:block;font-size:11px;font-weight:500}
.call b{font-size:18px;font-weight:500}
.nav{position:absolute;top:85px;left:0;width:1200px;font-size:15px;color:#fff;font-weight:500}
.nav span{position:absolute;white-space:nowrap}

/* hero */
.hero-title{left:103px;top:300px;font-size:56px;line-height:54px}
.hero-sub{left:103px;top:416px;font-size:22px;line-height:33px;color:var(--ink);width:480px}
.hero-photo{left:598px;top:70px;width:604px;height:634px;border-radius:50%;border:18px solid var(--blue);background:linear-gradient(135deg,#8a9b74,#c9c4b6 45%,#5d8fc4)}

/* features */
.feature{position:absolute;width:320px}
.feature .tick{position:absolute;left:0;top:4px}
.feature h3{margin-left:32px;font-size:19px;font-weight:500;color:var(--ink);white-space:nowrap}
.feature p{margin-left:32px;font-size:14px;line-height:24px;margin-top:3px}

/* welcome */
.welcome-bg{left:594px;top:1075px;width:606px;height:543px;background:var(--sky);border-top-right-radius:140px}
.welcome-photo{left:0;top:1075px;width:594px;height:543px;border-bottom-right-radius:70px;background:linear-gradient(120deg,#e6dccb,#c8ccd2 55%,#9aa6b0)}
.welcome{position:absolute;left:651px;top:1152px;width:460px}
.welcome-title{font-size:33px;line-height:40px;white-space:nowrap}
.welcome-text{margin-top:24px;font-size:13.5px;line-height:30.5px}
.welcome-text p+p{margin-top:10px}
.welcome .btn{position:static;margin-top:20px;width:155px;height:41px}

/* services */
.section-title{position:absolute;left:0;width:1200px;text-align:center}
.card{position:absolute;width:237px;height:299px;border:1px solid var(--line);border-radius:4px;background:#fff;text-align:center}
.card.active{box-shadow:0 4px 16px rgba(0,0,0,.12)}
.card svg{position:absolute;left:83px;top:24px}
.card h3{position:absolute;top:116px;width:100%;font-size:17.5px;font-weight:500;color:var(--ink);white-space:nowrap}
.card p{position:absolute;top:150px;left:8px;right:8px;font-size:12.3px;line-height:22.5px;color:#555}
.card .more{position:absolute;left:56px;top:236px;width:125px;height:31px;display:flex;align-items:center;justify-content:center;background:var(--green-soft);color:var(--green);font-size:11.5px;font-weight:600;border-radius:2px}
.card.active .more{background:var(--green);color:#fff}

/* booking */
.booking{left:0;top:2808px;width:1200px;height:529px;background:linear-gradient(90deg,rgba(10,55,95,.92),rgba(25,75,115,.82)),linear-gradient(90deg,#2d5a86,#7b8a92)}
.field{position:absolute;background:#fff;border-radius:2px;font-size:15px;color:#444;padding:15px 20px}

/* footer */
.site-footer{left:0;top:3337px;width:1200px;height:367px;background:var(--blue);color:#fff}
.fcol{position:absolute;top:70px}
.fcol h4{font-size:22px;font-weight:500;margin-bottom:14px}
.fcol a{display:block;font-size:15px;line-height:32px;color:#fff;text-decoration:none}
.vr{position:absolute;top:70px;width:1px;height:180px;background:rgba(255,255,255,.35)}
.contact-row{display:flex;gap:12px;align-items:center;font-size:15px;line-height:22px;margin-bottom:20px;white-space:nowrap}
.social{position:absolute;top:3555px;width:38px;height:38px;border:2px solid #fff;border-radius:50%}
</style>
</head>
<body>

<header class="site-header">
  <div class="brand" style="left:103px;top:10px;font-size:40px"><span class="dot" style="width:108px;height:108px"></span>Maplerose</div>
  <div class="abs call">
    <svg width="22" height="22" viewBox="0 0 24 24" fill="none" stroke="#fff" stroke-width="2"><path d="M5 3h4l2 5-3 2a12 12 0 0 0 6 6l2-3 5 2v4a2 2 0 0 1-2 2A18 18 0 0 1 3 5a2 2 0 0 1 2-2z"/></svg>
    <div><small>CALL US</small><b>888-888-8888</b></div>
  </div>
  <div class="btn" style="left:881px;top:17px;width:218px;height:40px">MAKE AN APPOINTMENT</div>
  <nav class="nav">
    <span style="left:477px">HOME</span><span style="left:547px">ABOUT</span><span style="left:628px">SERVICES</span><span style="left:724px">FAQ</span><span style="left:787px">RESOURCES</span><span style="left:902px">EMPLOYMENT</span><span style="left:1025px">CONTACT</span>
  </nav>
</header>

<section>
  <div class="abs hero-photo" role="img" aria-label="Smiling senior woman walking arm in arm with a caregiver in a garden"></div>
  <h1 class="abs serif hero-title">MAPLEROSE<br>HEALTH-CARE</h1>
  <p class="abs hero-sub">Sed ut perspiciatis unde omnis iste natus error sit voluptatem accusantium</p>
  <div class="btn" style="left:102px;top:503px;width:218px;height:42px">MAKE AN APPOINTMENT</div>
</section>

<section>
  <div class="feature" style="left:121px;top:790px"><svg class="tick" width="22" height="22"><circle cx="11" cy="11" r="11" fill="#dcecf6"/><path d="M6 11l3.5 3.5L16 8" stroke="#3c8ec2" stroke-width="2" fill="none"/></svg><h3>Choice of Caregiver</h3><p>Meet and select the caregiver of your choice.</p></div>
  <div class="feature" style="left:454px;top:790px"><svg class="tick" width="22" height="22"><circle cx="11" cy="11" r="11" fill="#dcecf6"/><path d="M6 11l3.5 3.5L16 8" stroke="#3c8ec2" stroke-width="2" fill="none"/></svg><h3>Professional &amp; Friendly Staff</h3><p>Our clients and their family are treated with respect and dignity.</p></div>
  <div class="feature" style="left:787px;top:790px"><svg class="tick" width="22" height="22"><circle cx="11" cy="11" r="11" fill="#dcecf6"/><path d="M6 11l3.5 3.5L16 8" stroke="#3c8ec2" stroke-width="2" fill="none"/></svg><h3>On Call 24/7</h3><p>We are always available with our 24/7 On Call service.</p></div>
  <div class="feature" style="left:121px;top:901px"><svg class="tick" width="22" height="22"><circle cx="11" cy="11" r="11" fill="#dcecf6"/><path d="M6 11l3.5 3.5L16 8" stroke="#3c8ec2" stroke-width="2" fill="none"/></svg><h3>Flexible Schedule</h3><p>Meet and select the caregiver of your choice.</p></div>
  <div class="feature" style="left:454px;top:901px"><svg class="tick" width="22" height="22"><circle cx="11" cy="11" r="11" fill="#dcecf6"/><path d="M6 11l3.5 3.5L16 8" stroke="#3c8ec2" stroke-width="2" fill="none"/></svg><h3>Free In Home Assessments</h3><p>We go to you to perform a professional needs assessment.</p></div>
  <div class="feature" style="left:787px;top:901px"><svg class="tick" width="22" height="22"><circle cx="11" cy="11" r="11" fill="#dcecf6"/><path d="M6 11l3.5 3.5L16 8" stroke="#3c8ec2" stroke-width="2" fill="none"/></svg><h3>Peace of Mind</h3><p>Knowing your loved one is being well cared for.</p></div>
</section>

<section>
  <div class="abs welcome-bg"></div>
  <div class="abs welcome-photo" role="img" aria-label="Caregiver supporting a smiling elderly woman using a walker indoors"></div>
  <div class="welcome">
    <h2 class="serif welcome-title">WELCOME TO<br>MAPLEROSE HEALTHCARE</h2>
    <div class="welcome-text">
      <p>At vero eos et accusamus et iusto odio dignqui blanditiis praesentium voluptatum deleniti atque corrupti quos s et quas molestias excepturi sint occaecati cupiditate non pdent, similique sunt in culpa qui officia deserunt mollitia animi, id est laborum et dolorum fuga.</p>
      <p>At vero eos et accusamus et iusto odio dignqui blanditiis praesentium voluptatum deleniti atque corrupti quos s et quas molestias excepturi sint occaecati cupiditate non pdent</p>
    </div>
    <div class="btn">LEARN MORE</div>
  </div>
</section>

<section>
  <h2 class="section-title serif" style="top:1702px;font-size:38px">OUR SERVICES</h2>
  <svg width="0" height="0" style="position:absolute"><defs>
    <symbol id="ic" viewBox="0 0 70 70"><g fill="none" stroke="#1f7f8c" stroke-width="2.4" stroke-linecap="round" stroke-linejoin="round"><rect x="12" y="16" width="46" height="40" rx="4"/><path d="M12 28h46"/><circle cx="35" cy="42" r="7" stroke="#5f9a3d"/></g></symbol>
  </defs></svg>

  <div class="card" style="left:102px;top:1783px"><svg width="70" height="70"><use href="#ic"/></svg><h3>Companion Care</h3><p>Sed ut perspiciatis une omnis iste nsit em accusantium doloremque laium, totam rem aperiam</p><div class="more">LEARN MORE</div></div>
  <div class="card" style="left:355px;top:1783px"><svg width="70" height="70"><use href="#ic"/></svg><h3>Transportation</h3><p>Sed ut perspiciatis une omnis iste nsit em accusantium doloremque laium, totam rem aperiam</p><div class="more">LEARN MORE</div></div>
  <div class="card active" style="left:609px;top:1783px"><svg width="70" height="70"><use href="#ic"/></svg><h3>Shopping &amp; Errands</h3><p>Sed ut perspiciatis une omnis iste nsit em accusantium doloremque laium, totam rem aperiam</p><div class="more">LEARN MORE</div></div>
  <div class="card" style="left:862px;top:1783px"><svg width="70" height="70"><use href="#ic"/></svg><h3>Light Housekeeping</h3><p>Sed ut perspiciatis une omnis iste nsit em accusantium doloremque laium, totam rem aperiam</p><div class="more">LEARN MORE</div></div>

  <div class="card" style="left:102px;top:2099px"><svg width="70" height="70"><use href="#ic"/></svg><h3>Stimulating Activities</h3><p>Sed ut perspiciatis une omnis iste nsit em accusantium doloremque laium, totam rem aperiam</p><div class="more">LEARN MORE</div></div>
  <div class="card" style="left:355px;top:2099px"><svg width="70" height="70"><use href="#ic"/></svg><h3>Correspondence</h3><p>Sed ut perspiciatis une omnis iste nsit em accusantium doloremque laium, totam rem aperiam</p><div class="more">LEARN MORE</div></div>
  <div class="card" style="left:609px;top:2099px"><svg width="70" height="70"><use href="#ic"/></svg><h3>Hygiene Assistance</h3><p>Sed ut perspiciatis une omnis iste nsit em accusantium doloremque laium, totam rem aperiam</p><div class="more">LEARN MORE</div></div>
  <div class="card" style="left:862px;top:2099px"><svg width="70" height="70"><use href="#ic"/></svg><h3>Ambulation Assistance</h3><p>Sed ut perspiciatis une omnis iste nsit em accusantium doloremque laium, totam rem aperiam</p><div class="more">LEARN MORE</div></div>

  <div class="card" style="left:102px;top:2417px"><svg width="70" height="70"><use href="#ic"/></svg><h3>Meal Preparation</h3><p>Sed ut perspiciatis une omnis iste nsit em accusantium doloremque laium, totam rem aperiam</p><div class="more">LEARN MORE</div></div>
  <div class="card" style="left:355px;top:2417px"><svg width="70" height="70"><use href="#ic"/></svg><h3>Medication Reminders</h3><p>Sed ut perspiciatis une omnis iste nsit em accusantium doloremque laium, totam rem aperiam</p><div class="more">LEARN MORE</div></div>
  <div class="card" style="left:609px;top:2417px"><svg width="70" height="70"><use href="#ic"/></svg><h3>Laundry &amp; Linens</h3><p>Sed ut perspiciatis une omnis iste nsit em accusantium doloremque laium, totam rem aperiam</p><div class="more">LEARN MORE</div></div>
  <div class="card" style="left:862px;top:2417px"><svg width="70" height="70"><use href="#ic"/></svg><h3>Kitchen &amp; Bathroom</h3><p>Sed ut perspiciatis une omnis iste nsit em accusantium doloremque laium, totam rem aperiam</p><div class="more">LEARN MORE</div></div>
</section>

<section>
  <div class="abs booking" role="img" aria-label="Caregiver checking an elderly man's blood pressure, under a dark blue overlay"></div>
  <h2 class="section-title serif" style="top:2876px;font-size:34px;color:#fff">THE BEST HOME CARE STARTS HERE</h2>
  <p class="section-title" style="top:2926px;font-size:20px;color:#fff">Flexible appointments and care options.</p>
  <div class="field" style="left:263px;top:2982px;width:335px;height:49px">Name</div>
  <div class="field" style="left:611px;top:2982px;width:335px;height:49px">Name</div>
  <div class="field" style="left:263px;top:3045px;width:335px;height:49px">Name</div>
  <div class="field" style="left:611px;top:3045px;width:335px;height:49px">Name</div>
  <div class="field" style="left:263px;top:3110px;width:683px;height:92px">Name</div>
  <div class="btn" style="left:790px;top:3219px;width:156px;height:40px">SUBMIT</div>
</section>

<footer class="abs site-footer">
  <div class="fcol" style="left:101px"><h4>Quick Links</h4><a>Home</a><a>About</a><a>Services</a><a>Employment</a><a>Contact</a></div>
  <div class="vr" style="left:253px"></div>
  <div class="fcol" style="left:286px"><h4>Other Links</h4><a>Privacy Policy</a><a>Terms of Service</a><a>Credit</a><a>FAQ</a></div>
  <div class="vr" style="left:443px"></div>
  <div class="fcol" style="left:484px"><h4>Contact Us</h4>
    <div class="contact-row"><svg width="38" height="38"><circle cx="19" cy="19" r="19" fill="#fff"/><path d="M19 10a6 6 0 0 0-6 6c0 5 6 12 6 12s6-7 6-12a6 6 0 0 0-6-6z" fill="var(--blue)"/><circle cx="19" cy="16" r="2.2" fill="#fff"/></svg><span>1234 Somestreet<br>&nbsp;Anywhere USA 21212</span></div>
    <div class="contact-row"><svg width="38" height="38"><circle cx="19" cy="19" r="19" fill="#fff"/><path d="M13 11h4l2 4-2 2a9 9 0 0 0 5 5l2-2 4 2v4a2 2 0 0 1-2 1A15 15 0 0 1 12 13a2 2 0 0 1 1-2z" fill="var(--blue)"/></svg><span>888 888 8888</span></div>
    <div class="contact-row"><svg width="38" height="38"><circle cx="19" cy="19" r="19" fill="#fff"/><rect x="11" y="13" width="16" height="12" rx="1" fill="var(--blue)"/><path d="M11 14l8 6 8-6" stroke="#fff" stroke-width="1.5" fill="none"/></svg><span>info@maplerosehealthcare.com</span></div>
  </div>
  <div class="vr" style="left:742px;top:50px;height:40px"></div>
  <div class="brand" style="left:769px;top:70px;font-size:30px"><span class="dot" style="width:86px;height:86px;border-width:5px"></span>Maplerose</div>
  <div class="abs" style="left:101px;top:307px;width:999px;height:1px;background:rgba(255,255,255,.45)"></div>
  <p class="abs" style="left:0;top:325px;width:1200px;text-align:center;font-size:13px">Copyright © 2022 MAPLEROSE-HEALTH-CARE All rights reserved.</p>
</footer>
<span class="social" style="left:855px"></span>
<span class="social" style="left:902px"></span>
<span class="social" style="left:949px"></span>
<span class="social" style="left:996px"></span>

</body>
</html>
```